Business Card Design Project

I need a business card with the logo i have selected with a heading of
Repairs
Restretching
Cleaning
Supply and lay all in that order
call 0438270915
www.rugmendclinic.example

colours used should be bold and clear and match the logo, thinking white background with black writing
a mixture of fonts is okay but Repairs, Cleaning, Supply and Lay should all be the same as they are the main points...
kind regards wes
update to all designers i would like my name on the business card Wes Burnell i think it would look good above the phone number
Updates

can you please add my name on the business card

Wes Burnell

i think it would look best above the phone numberĀ 

Industry/Entity Type

Business

```html
<!DOCTYPE html>
<html lang="en">
<head>
<meta charset="utf-8">
<title>Rug Mend Clinic – Business Card</title>
<link rel="stylesheet" href="https://fonts.googleapis.com/css2?family=Roboto+Condensed:wght@700&family=Roboto:wght@400;700&display=swap">
<style>
  :root {
    --backdrop: #c8c8c8;
    --card: #ffffff;
    --navy: #163a5c;
    --red: #e8262c;
    --orange: #f7941d;
    --ink: #111111;
    --skin: #e9c9a0;
    --rug: #c99a5b;
  }
  * { margin: 0; padding: 0; box-sizing: border-box; }
  html, body {
    width: 1200px; height: 900px; overflow: hidden;
    background: var(--backdrop);
  }
  .card {
    position: absolute; left: 100px; top: 165px;
    width: 1000px; height: 570px;
    background: var(--card);
    border-radius: 30px;
    overflow: hidden;
  }
  .stripes { position: absolute; inset: 0; }
  .mascot {
    position: absolute; left: 110px; top: 30px;
    width: 320px; height: 320px;
    border-radius: 50%;
    border: 8px solid var(--red);
    background: radial-gradient(circle at 50% 45%, var(--skin), var(--rug) 70%, #a87a3e);
  }
  .brand-plate {
    position: absolute; left: 30px; top: 370px;
    width: 450px; height: 170px;
    background: var(--card);
    border-radius: 18px;
  }
  .brand-name {
    position: absolute; left: 30px; top: 380px; width: 450px;
    text-align: center;
    font-family: "Roboto Condensed", sans-serif; font-weight: 700;
    color: var(--navy); text-transform: uppercase;
    line-height: 1;
  }
  .brand-name .line-main { display: block; font-size: 82px; }
  .brand-name .line-sub { display: block; font-size: 62px; margin-top: 6px; }
  .services {
    position: absolute; right: 40px; top: 38px;
    list-style: none; text-align: right;
    font-family: "Roboto Condensed", sans-serif; font-weight: 700;
    font-size: 38px; line-height: 1;
  }
  .services li { margin-bottom: 36px; color: var(--navy); }
  .services li:last-child { margin-bottom: 0; }
  .services .accent { color: var(--red); }
  .contact-band {
    position: absolute; left: 505px; right: 0; top: 378px; height: 130px;
    background: var(--orange);
    font-family: Roboto, sans-serif;
  }
  .contact-name {
    position: absolute; left: 0; width: 440px; top: 8px; text-align: center;
    color: #fff; font-size: 34px; font-weight: 400; line-height: 1.1;
  }
  .contact-phone {
    position: absolute; left: 30px; top: 48px;
    color: var(--ink); font-size: 44px; font-weight: 700; letter-spacing: 0.5px; line-height: 1;
  }
  .contact-web {
    position: absolute; left: 22px; top: 100px;
    color: var(--ink); font-size: 22px; font-weight: 700; line-height: 1;
  }
</style>
</head>
<body>
  <section class="card" aria-label="Rug Mend Clinic business card">
    <svg class="stripes" width="1000" height="570" viewBox="0 0 1000 570" aria-hidden="true">
      <polygon points="170,0 255,0 585,570 500,570" fill="var(--red)"/>
      <polygon points="460,0 492,0 822,570 790,570" fill="var(--navy)"/>
      <polygon points="-240,0 -218,0 112,570 90,570" fill="var(--navy)"/>
      <polygon points="-330,0 -255,0 75,570 0,570" fill="var(--red)"/>
      <polygon points="-40,160 -15,160 225,570 200,570" fill="var(--navy)"/>
      <polygon points="-80,230 -10,230 200,570 130,570" fill="var(--red)"/>
    </svg>

    <div class="mascot" role="img" aria-label="Cartoon carpet repairman mascot carrying a rolled rug and a first-aid case"></div>

    <div class="brand-plate"></div>
    <h1 class="brand-name">
      <span class="line-main">Rug Mend</span>
      <span class="line-sub">Clinic</span>
    </h1>

    <ul class="services">
      <li>Repairs</li>
      <li class="accent">Restretching</li>
      <li>Cleaning</li>
      <li>Supply and lay</li>
    </ul>

    <div class="contact-band">
      <p class="contact-name">Wes Burnell</p>
      <p class="contact-phone">call 0438270915</p>
      <p class="contact-web">www.rugmendclinic.example</p>
    </div>
  </section>
</body>
</html>
```